One Page Sales Flyer for Wireless Survey- Computer Hardware

I want a designer to create a one page 4 color sales slick to be given to our sales team to sell to the end customers. I would like a visual picture of a heat map so vornix "heat map wireless" to get an idea of how that image should look.

```html
<!DOCTYPE html>
<html lang="en">
<head>
<meta charset="utf-8">
<title>Arbor – Wireless Site Survey Sales Flyer</title>
<link href="https://fonts.googleapis.com/css2?family=Michroma&family=Open+Sans:wght@400;600&display=swap" rel="stylesheet">
<style>
  :root{
    --blue:#3a9de0;
    --blue-pale:#cfe6f8;
    --navy:#263845;
    --ink:#2d2f33;
    --stage:#e4e7ea;
    --white:#ffffff;
  }
  *{margin:0;padding:0;box-sizing:border-box}
  html,body{width:1200px;height:582px;overflow:hidden;background:var(--stage)}
  .canvas{position:relative;width:1200px;height:582px}
  .flyer{
    position:absolute;left:394px;top:0;width:515px;height:728px;
    transform:scale(0.8);transform-origin:top left;
    background:linear-gradient(180deg,#f7f8fa 0%,#eceff2 60%,#f5f6f8 100%);
    font-family:"Open Sans",Arial,sans-serif;color:var(--ink);overflow:hidden;
  }
  .heading{font-family:"Michroma","Arial Black",sans-serif;text-transform:uppercase;font-weight:400}

  /* brand */
  .brand{position:absolute;left:10px;top:0;width:160px;height:130px;background:var(--white);
    display:flex;flex-direction:column;align-items:center;justify-content:center;gap:8px}
  .brand__mark{width:40px;height:40px;background:var(--blue);border-radius:6px}
  .brand__name{font-size:24px;color:var(--ink);letter-spacing:1px}

  /* target customers column */
  .sidebar{position:absolute;left:10px;top:133px;width:160px;height:590px;background:var(--blue)}
  .sidebar__title{position:absolute;left:0;top:10px;width:160px;text-align:center;color:var(--white);line-height:1}
  .sidebar__title .big{display:block;font-size:22px}
  .sidebar__title .small{display:block;font-size:14px;margin-top:3px}
  .sidebar__list{position:absolute;left:8px;top:58px;width:144px;height:280px;background:var(--blue-pale);
    clip-path:polygon(0 0,100% 0,100% 90%,50% 100%,0 90%);list-style:none;padding:4px 0 0 8px}
  .sidebar__list li{font-size:13px;font-weight:600;color:var(--ink);height:26.2px;display:flex;align-items:center;white-space:nowrap}
  .sidebar__list li::before{content:"";width:6px;height:6px;border-radius:50%;background:var(--blue);margin-right:6px;flex:none}
  .sidebar__photo{position:absolute;left:8px;top:333px;width:144px;height:250px;
    background:linear-gradient(160deg,#e9ecef 0%,#cfc8c4 45%,#8b3a3d 75%,#5a3b33 100%)}

  /* header banner with map */
  .banner{position:absolute;left:196px;top:0;width:296px;height:320px}
  .banner svg{position:absolute;inset:0}
  .banner__title{position:absolute;left:0;top:10px;width:296px;text-align:center;color:var(--white);line-height:1}
  .banner__title .l1,.banner__title .l2{display:block;font-size:34px;letter-spacing:-.5px}
  .banner__title .l2{margin-top:2px}
  .banner__title .l3{display:block;font-size:11px;margin-top:5px;line-height:1.05}
  .banner__map{position:absolute;left:22px;top:140px;width:252px;height:150px;border-radius:18px;
    background:
      radial-gradient(ellipse at 50% 10%,rgba(79,179,230,.9) 0%,rgba(79,179,230,0) 45%),
      linear-gradient(180deg,#4fb3e6 0%,#5cc46a 28%,#e6e23a 50%,#f2a03a 72%,#e43b30 100%)}

  /* body copy */
  .copy{position:absolute;left:196px;top:322px;width:296px}
  .copy h2{font-size:13px;color:var(--blue);line-height:1.08;margin-top:8px}
  .copy p{font-size:9px;line-height:1.33;text-align:justify;margin-top:4px}
  .copy ol{list-style:none;counter-reset:n;margin-top:4px}
  .copy li{counter-increment:n;position:relative;padding-left:14px;font-size:9px;line-height:1.25;margin-bottom:3px}
  .copy li::before{content:counter(n) ".";position:absolute;left:0;color:var(--blue);font-weight:600}

  /* contact bar */
  .contact{position:absolute;left:172px;top:662px;width:343px;height:40px;background:var(--navy);
    clip-path:polygon(0 50%,18px 0,100% 0,100% 100%,18px 100%);
    display:flex;align-items:center;justify-content:center;gap:8px;color:var(--white);font-size:10.4px;font-weight:600}
  .contact .sep{color:var(--blue)}
  .footnote{position:absolute;left:172px;top:710px;width:343px;text-align:center;font-size:7.6px;color:var(--ink)}
</style>
</head>
<body>
<div class="canvas">
  <article class="flyer">
    <header class="brand">
      <span class="brand__mark"></span>
      <span class="brand__name">ARBOR</span>
    </header>

    <aside class="sidebar">
      <h2 class="sidebar__title heading"><span class="big">Target</span><span class="small">Customers</span></h2>
      <ul class="sidebar__list">
        <li>Distributors</li>
        <li>Warehouses</li>
        <li>SLED</li>
        <li>K-12</li>
        <li>Medical / Hospitals</li>
        <li>Enterprise F1000</li>
        <li>Sports Venues</li>
        <li>Stadiums</li>
        <li>Hotels</li>
        <li>Retail stores</li>
      </ul>
      <div class="sidebar__photo" role="img" aria-label="Photo of a smiling woman working at a table with a tablet and a water carafe"></div>
    </aside>

    <section class="banner">
      <svg width="296" height="320" viewBox="0 0 296 320" aria-hidden="true">
        <polygon points="2,0 294,0 294,280 148,318 2,280" fill="rgba(255,255,255,.85)" stroke="#3a9de0" stroke-width="4"/>
        <rect x="0" y="0" width="296" height="112" fill="#3a9de0"/>
      </svg>
      <h1 class="banner__title heading">
        <span class="l1">Increase</span>
        <span class="l2">Hardware</span>
        <span class="l3">And services spend with<br>wireless site surveys</span>
      </h1>
      <div class="banner__map" role="img" aria-label="3D heat map of the United States shaded from blue in the north to red in the south"></div>
    </section>

    <main class="copy">
      <h2 class="heading">What is a wireless site survey or heat map?</h2>
      <p>A wireless site survey is a compilation of reports showing a visual representation of health of your wireless network. This does not only show how strong or weak a wireless signal is in any location it also helps aid in channel and placement to ensure maximum stable data rates are archived even where the single appears strong.</p>
      <h2 class="heading">Why do customers need a site survey?</h2>
      <p>Any variety of factors can contribute to an unhealthy wireless network (electrical, motors, materials used in construction, distance, neighboring wireless networks, etc.) and traditional methods that use only blueprints and a computer program to show signal strength have shown to be ineffective.</p>
      <h2 class="heading">Why should they use you?</h2>
      <ol>
        <li>42% of businesses report some issues with wireless connectivity and acknowledge its effect on the bottom line*</li>
        <li>Most of these problems are solved through either fine tuning the current equipment (managed services) or purchasing new equipment (incremental sales) of which you can provide both</li>
        <li>Being a one-stop shop for all your customer’s IT needs prevents them from needing additional vendors</li>
        <li>The increase of IoT (Internet of things) and BYOD (Bring Your Own Device)</li>
      </ol>
    </main>

    <footer class="contact">
      <span>www.yourarbor.com</span><span class="sep">|</span>
      <span>info@yourarbor.com</span><span class="sep">|</span>
      <span>555-014-2270</span>
    </footer>
    <p class="footnote">*Newsline.com. “Connectivity in the Modern Enterprise”. June 2017</p>
  </article>
</div>
</body>
</html>
```